Vorn Solutions: searching for a flyer to trow in letterboxes for properties we are interested in

Hello ,

Introduction:
We are a company based in Luxembourg called "Vorn Solutions". We are specialized in buying properties on which we develop and build constructions before selling them.

Informations for the flyer:
We need a flyer to trow into the letter boxes of property owners letting them know that we are interested in buying their property, if they are interested they can give us a call.

The text for the flyer/letter is in the attachment called >>2020-03-11_VS_Text for flyer,letter there might be slight changes<<.

We need to look competent, professional and financially stable.

The flyer needs to be short and not over welling with information otherwise it will land in the trash.

We have decided that we don't want real pictures on the flyer, but shapes of any kind, blue prints, drawings are fine.

Format should be in DIN A4. We plan to print the flyer on both sides in two different languages, in other words the design will be the same on both sides only the text will be in a different language.

I also added our current logo and here is the design of the website that is under construction at the moment http://www.vornsolutions.example/. The logo's color can be changed into a different blue or uni color (all white or all black).
Updates

Hi, First time user the howl thing started faster as expected. Furthermore, I need to catch my boss to discust the project with him and he is on a lot of meetings. Please give us a little bit more time. Thanks

Target Market(s)

Property owners

Requirements
Must have
• email, phone number, tax number (RCS), Tax number , matriculation and address.
see word file in attachment for information
Nice to have
• Our company logo, in one form or an other, you can be creative, the logo is in the attachment.
Should not have
• Real pictures

```html
<!DOCTYPE html>
<html lang="fr">
<head>
<meta charset="utf-8">
<title>Vorn Solutions – Courrier propriétaires</title>
<link rel="stylesheet" href="https://fonts.googleapis.com/css2?family=Bebas+Neue&family=Roboto:wght@400&display=swap">
<style>
  :root {
    --brand-blue: #156bb6;
    --ink-dark: #111111;
    --header-tint: #f0f5f7;
    --paper: #ffffff;
  }
  * { margin: 0; padding: 0; box-sizing: border-box; }
  html, body { width: 856px; height: 1200px; overflow: hidden; background: var(--paper); }
  .sheet { position: relative; width: 856px; height: 1200px; background: var(--paper); font-family: "Roboto", Arial, sans-serif; color: var(--brand-blue); }

  .letterhead { position: absolute; left: 13px; top: 66px; width: 415px; height: 115px; background: var(--header-tint); }
  .letterhead__name { position: absolute; left: 94px; top: 30px; font-family: "Bebas Neue", "Arial Narrow", sans-serif; font-size: 42px; letter-spacing: 0.5px; line-height: 1; white-space: nowrap; }
  .letterhead__address { position: absolute; left: 97px; top: 78px; font-size: 12.5px; letter-spacing: 0.2px; white-space: nowrap; }

  .brand-mark { position: absolute; display: flex; align-items: center; gap: 8px; font-family: "Bebas Neue", "Arial Narrow", sans-serif; color: var(--brand-blue); white-space: nowrap; line-height: 1; }
  .brand-mark__square { background: var(--brand-blue); flex: none; }
  .brand-mark--top { left: 648px; top: 144px; font-size: 27px; }
  .brand-mark--top .brand-mark__square { width: 18px; height: 18px; }

  .letter-body { position: absolute; left: 107px; top: 246px; width: 680px; font-size: 16.8px; line-height: 21px; letter-spacing: 0.4px; }
  .letter-body p { position: absolute; left: 0; width: 680px; white-space: nowrap; }
  .greeting { top: 0; }
  .para-intro { top: 62px; }
  .para-offer { top: 167px; }
  .para-closing { top: 229px; }
  .salutation { top: 313px; }
  .signature { top: 396px; }

  .footer { position: absolute; left: 13px; top: 795px; width: 830px; height: 405px; background: var(--brand-blue); border-radius: 48px 48px 0 0; }
  .footer__panel { position: absolute; left: 47px; top: 0; width: 733px; height: 343px; background: var(--paper); border-radius: 0 0 32px 32px; }
  .brand-mark--footer { left: 50%; top: 186px; transform: translateX(-50%); font-size: 44px; gap: 12px; }
  .brand-mark--footer .brand-mark__square { width: 30px; height: 30px; }

  .contact-row { position: absolute; left: 0; top: 282px; width: 733px; height: 30px; padding: 0 22px; display: flex; justify-content: space-between; align-items: center; }
  .contact { display: flex; align-items: center; gap: 10px; font-size: 15px; letter-spacing: 0.4px; white-space: nowrap; color: var(--brand-blue); }
  .contact svg { width: 21px; height: 21px; flex: none; }
</style>
</head>
<body>
<div class="sheet">

  <header class="letterhead">
    <div class="letterhead__name">VORN SOLUTIONS SÀRL</div>
    <div class="letterhead__address">17 RUE DES ATELIERS, L-3290 BETTEMBOURG</div>
  </header>

  <div class="brand-mark brand-mark--top"><span class="brand-mark__square"></span>VORN SOLUTIONS</div>

  <main class="letter-body">
    <p class="greeting">Madame, Monsieur,</p>
    <p class="para-intro">Ce courrier vous a été adressé, car votre propriété a attiré notre attention.<br>Nous souhaiterions discuter avec vous de son éventuel rachat par notre<br>société.</p>
    <p class="para-offer">En cas d’accord, nous vous assurons une décision rapide, un paiement<br>garanti, et zéro frais d’intermédiaire.</p>
    <p class="para-closing">En attendant de vos nouvelles, nous restons à votre entière disposition pour<br>tout renseignement.</p>
    <p class="salutation">Salutations distinguées,</p>
    <p class="signature">L’équipe de Vorn Solutions</p>
  </main>

  <footer class="footer">
    <div class="footer__panel">
      <div class="brand-mark brand-mark--footer"><span class="brand-mark__square"></span>VORN SOLUTIONS</div>

      <div class="contact-row">
        <div class="contact contact--phone">
          <svg viewBox="0 0 24 24" fill="none" stroke="currentColor" stroke-width="1.3" stroke-linejoin="round" aria-hidden="true">
            <path d="M5 3.5l3 0.5 1.5 4-2 1.5c1 2.5 3 4.5 5.5 5.5l1.5-2 4 1.5 0.5 3c-0.2 1.5-1.5 2.5-3 2.3C9.5 19 5 14.5 3.2 8c-0.2-1.5 0.3-4 1.8-4.5z"/>
            <path d="M14 3.5a6.5 6.5 0 0 1 6.5 6.5M14 6.5a3.5 3.5 0 0 1 3.5 3.5"/>
          </svg>
          <span>691 000 482</span>
        </div>
        <div class="contact contact--mail">
          <svg viewBox="0 0 24 24" fill="none" stroke="currentColor" stroke-width="1.3" stroke-linejoin="round" aria-hidden="true">
            <path d="M21 3L3 11l6 2.5L21 3l-9 12v5l3-4 4 3z"/>
            <path d="M6 17l-3 3M8 19l-2 2"/>
          </svg>
          <span>info@vornsolutions.example</span>
        </div>
        <div class="contact contact--web">
          <svg viewBox="0 0 24 24" fill="none" stroke="currentColor" stroke-width="1.4" aria-hidden="true">
            <circle cx="12" cy="12" r="9.5"/>
            <ellipse cx="12" cy="12" rx="4" ry="9.5"/>
            <path d="M2.5 12h19M4 7h16M4 17h16"/>
          </svg>
          <span>www.vornsolutions.example</span>
        </div>
      </div>
    </div>
  </footer>

</div>
</body>
</html>
```